British Columbia Day banner showcasing 20% off site

Banner graphic promoting our BC Day sale
Size: 1800 x 1000
- flag has been uploaded for inspiration
- examples from other companies and their sale banners have been uploaded for inspiration.
- product images can be found at www.mygreenleafhub.com, please use a variety of different products in this banner

Target Market(s)

19+

Industry/Entity Type

Cannabis

Requirements
Must have
• Phrases:
- “Celebrate BC Day with BC bud and companies”
- “20% off site wide sale*"
- Underneath phrase the date of sale “July 30th - August 3rd”
- In tiny print “*excludes all sale and bundled items”
- MUST BE 1800 X1000
Nice to have
• - images of the products or bud we carry which can be found at www.mygreenleafhub.com
- bold
Should not have
• - company logo

```html
<!DOCTYPE html>
<html lang="en">
<head>
<meta charset="utf-8">
<title>BC Day Sale Banner</title>
<link rel="stylesheet" href="https://fonts.googleapis.com/css2?family=Archivo:wght@400;700;900&family=Kaushan+Script&display=swap">
<style>
  :root {
    --page-bg: #adc4fb;
    --banner-yellow: #fccb19;
    --faint-disc: #f2c43c;
    --bud-dark: #6b6a4a;
    --bud-light: #8d8a5c;
    --white: #ffffff;
    --red: #e31b3f;
    --red-shade: #d21f38;
    --navy: #283278;
    --navy-star: #15294b;
    --sale-yellow: #fff200;
    --ink: #111111;
    --badge-red: #e8342e;
    --badge-orange: #e94e1b;
  }
  html, body {
    margin: 0;
    padding: 0;
    width: 1200px;
    height: 1200px;
    overflow: hidden;
    background: var(--page-bg);
  }
  .sale-banner {
    position: absolute;
    left: 0;
    top: 266px;
    width: 1200px;
    height: 667px;
    display: block;
  }
  .script { font-family: "Kaushan Script", cursive; }
  .bold-sans { font-family: "Archivo", Arial, sans-serif; }
</style>
</head>
<body>
<svg class="sale-banner" viewBox="0 0 1200 667" xmlns="http://www.w3.org/2000/svg" aria-label="Celebrate BC Day – 20% off site wide sale">
  <defs>
    <polygon id="star" points="0,-1 .225,-.309 .951,-.309 .363,.118 .588,.809 0,.382 -.588,.809 -.363,.118 -.951,-.309 -.225,-.309"/>
    <radialGradient id="bud-tone" cx="50%" cy="45%" r="60%">
      <stop offset="0" stop-color="var(--bud-light)"/>
      <stop offset="1" stop-color="var(--bud-dark)"/>
    </radialGradient>
    <linearGradient id="badge-tone" x1="0" y1="0" x2="0" y2="1">
      <stop offset="0" stop-color="var(--badge-red)"/>
      <stop offset="1" stop-color="var(--badge-orange)"/>
    </linearGradient>
    <clipPath id="banner-clip"><rect width="1200" height="667"/></clipPath>
  </defs>

  <g clip-path="url(#banner-clip)">
    <rect class="banner-bg" width="1200" height="667" fill="var(--banner-yellow)"/>

    <g class="faint-discs" fill="var(--faint-disc)" opacity="0.7">
      <circle cx="764" cy="114" r="118"/>
      <circle cx="381" cy="467" r="110"/>
      <circle cx="1161" cy="342" r="52"/>
      <circle cx="0" cy="300" r="65"/>
      <circle cx="690" cy="680" r="95"/>
    </g>

    <g class="product-buds" fill="url(#bud-tone)">
      <ellipse role="img" aria-label="Cannabis bud product photo" cx="55" cy="18" rx="68" ry="26"/>
      <ellipse role="img" aria-label="Cannabis bud product photo" cx="153" cy="240" rx="68" ry="46" transform="rotate(-20 153 240)"/>
      <ellipse role="img" aria-label="Cannabis bud product photo" cx="1125" cy="58" rx="82" ry="52" transform="rotate(-25 1125 58)"/>
      <ellipse role="img" aria-label="Cannabis bud product photo" cx="1076" cy="288" rx="50" ry="38" transform="rotate(-35 1076 288)"/>
      <ellipse role="img" aria-label="Cannabis bud product photo" cx="62" cy="620" rx="75" ry="50" transform="rotate(-30 62 620)"/>
      <ellipse role="img" aria-label="Cannabis bud product photo" cx="512" cy="660" rx="44" ry="26"/>
      <ellipse role="img" aria-label="Cannabis bud product photo" cx="892" cy="592" rx="46" ry="34" transform="rotate(30 892 592)"/>
    </g>

    <g class="stars">
      <use href="#star" fill="var(--navy-star)" transform="translate(363 81) rotate(12) scale(31)"/>
      <use href="#star" fill="var(--navy-star)" transform="translate(135 452) rotate(8) scale(30)"/>
      <use href="#star" fill="var(--navy-star)" transform="translate(374 603) rotate(10) scale(20)"/>
      <use href="#star" fill="var(--red)" transform="translate(78 129) rotate(-8) scale(20)"/>
      <use href="#star" fill="var(--red)" transform="translate(845 125) rotate(-8) scale(17)"/>
      <use href="#star" fill="var(--red)" transform="translate(1010 184) rotate(8) scale(20)"/>
      <use href="#star" fill="var(--red)" transform="translate(274 320) rotate(-10) scale(21)"/>
      <use href="#star" fill="var(--red)" transform="translate(911 372) rotate(10) scale(27)"/>
      <use href="#star" fill="var(--red)" transform="translate(216 611) rotate(-8) scale(20)"/>
    </g>

    <g class="headline-stack" transform="rotate(-6 588 300)">
      <rect class="celebrate-panel" x="385" y="68" width="405" height="130" fill="var(--white)"/>
      <rect class="bc-day-panel" x="320" y="185" width="530" height="222" fill="var(--red)"/>
      <polygon class="bc-day-shade" points="600,185 850,185 850,407 420,407" fill="var(--red-shade)"/>
      <rect class="discount-panel" x="385" y="396" width="405" height="140" fill="var(--navy)"/>

      <text class="script" x="588" y="172" font-size="84" text-anchor="middle" fill="var(--ink)">Celebrate</text>
      <text class="bold-sans" x="588" y="338" font-size="152" font-weight="900" text-anchor="middle" fill="var(--white)" textLength="470" lengthAdjust="spacingAndGlyphs">BC DAY</text>
      <text class="bold-sans" x="588" y="385" font-size="38" font-weight="700" text-anchor="middle" fill="var(--white)">BC Vendors and BC Bud</text>
      <text class="bold-sans" x="588" y="482" font-size="96" font-weight="900" text-anchor="middle" fill="var(--sale-yellow)" textLength="330" lengthAdjust="spacingAndGlyphs">20% OFF</text>
      <text class="bold-sans" x="588" y="522" font-size="32" font-weight="400" text-anchor="middle" fill="var(--white)">SITE WIDE SALE</text>
      <use href="#star" fill="var(--red)" transform="translate(453 512) scale(10)"/>
      <use href="#star" fill="var(--red)" transform="translate(723 512) scale(10)"/>
      <text class="bold-sans" x="588" y="568" font-size="26" font-weight="700" text-anchor="middle" fill="var(--ink)">JULY 30<tspan font-size="15" dy="-11">TH</tspan><tspan dy="11"> - AUGUST 3</tspan><tspan font-size="15" dy="-11">RD</tspan></text>
    </g>

    <g class="exclusion-badge">
      <circle role="img" aria-label="Round badge with British Columbia flag motif" cx="1056" cy="525" r="96" fill="url(#badge-tone)"/>
      <g class="bold-sans" font-size="19" font-weight="700" fill="var(--white)" text-anchor="middle">
        <text x="1056" y="497">EXCLUDES</text>
        <text x="1056" y="522">ALL SALE AND</text>
        <text x="1056" y="547">BUNDLED</text>
        <text x="1056" y="572">ITEMS</text>
      </g>
    </g>
  </g>
</svg>
</body>
</html>
```